Veterinary Clinic Letterhead - Ridgeview Veterinary Surgery

We need a letterhead design for an established Veterinary Clinic in Mareeba called Ridgeview Veterinary Surgery. We are a moderate sized mixed animal veterinary clinic offering a wide variety of veterinary services. The design should use the same colour pattern as those in the logos supplied. The design should also include our address (48 Tulloch Road, Tallowood Vale, Queensland, 4891), phone number (07 4158 6734), email (admin@ridgeviewvets.com.au), website (www.ridgeviewvets.com.au) and our opening hours (8am to 5pm Monday to Friday and 8am to 12pm Saturday).
Target Market(s)
Pet owners
Industry/Entity Type
Veterinary
Requirements
Must have
- The logo or modification of it, business address, opening hours, website, phone number and email address

```html
<!DOCTYPE html>
<html lang="en">
<head>
<meta charset="utf-8">
<title>Ridgeview Veterinary Surgery – Letterhead</title>
<link href="https://fonts.googleapis.com/css2?family=Inter:wght@400;600&family=Arimo:wght@400&display=swap" rel="stylesheet">
<style>
  :root {
    --navy: #0b2d5b;
    --ink: #1c2433;
    --body-text: #4a4d53;
    --backdrop: #acabad;
    --paper-top: #ffffff;
    --paper-bottom: #dfdfe1;
    --mark-tint: rgba(11, 45, 91, 0.045);
  }
  * { margin: 0; padding: 0; box-sizing: border-box; }
  html, body {
    width: 1039px; height: 1200px; overflow: hidden;
    background: var(--backdrop);
  }
  .letterhead {
    position: absolute; left: 159px; top: 99px;
    width: 710px; height: 1001px; overflow: hidden;
    background: linear-gradient(150deg, var(--paper-top) 20%, var(--paper-bottom) 100%);
    box-shadow: 0 1px 4px rgba(0,0,0,0.25);
    font-family: "Arimo", Arial, sans-serif;
  }
  .brand {
    position: absolute; left: 51px; top: 51px; width: 134px;
    text-align: center; color: var(--navy);
    font-family: "Inter", sans-serif; font-weight: 400;
  }
  .brand-dot {
    display: block; width: 66px; height: 66px; margin: 0 auto 6px;
    border-radius: 50%; background: var(--navy);
  }
  .brand-name { font-size: 9.6px; letter-spacing: 0.4px; line-height: 11px; white-space: nowrap; }
  .brand-sub { font-size: 6px; letter-spacing: 3px; line-height: 8px; }
  .contact {
    position: absolute; left: 473px; top: 52px;
    font-family: "Inter", sans-serif; font-size: 12.6px; color: var(--ink);
    list-style: none;
  }
  .contact li { display: flex; align-items: flex-start; line-height: 15.2px; }
  .contact .address { margin-bottom: 6px; }
  .contact svg { width: 10px; height: 10px; margin: 3px 6px 0 0; flex: none; fill: var(--navy); }
  .watermark {
    position: absolute; left: 93px; top: 258px;
    width: 516px; height: 516px; border-radius: 50%;
    background: var(--mark-tint);
  }
  .letter {
    position: absolute; left: 53px; top: 334px; width: 600px;
    color: var(--body-text);
  }
  .salutation { font-size: 15.6px; line-height: 20px; margin-bottom: 16px; }
  .letter p.body {
    font-size: 10.8px; line-height: 16.8px; text-align: justify;
    hyphens: auto; margin-bottom: 16.8px;
  }
  .closing { font-size: 10.8px; line-height: 16.8px; }
  .signature {
    display: block; width: 90px; height: 34px; margin-top: 14px;
    background: linear-gradient(90deg, rgba(28,36,51,0.16), rgba(28,36,51,0.03));
    border-radius: 4px;
  }
  .footer-band { position: absolute; left: 0; top: 870px; width: 710px; height: 131px; }
  .hours {
    position: absolute; left: 0; right: 0; top: 971px;
    text-align: center; color: #ffffff;
    font-family: "Inter", sans-serif; font-size: 12px; line-height: 16px;
  }
  .hours strong { font-weight: 600; }
</style>
</head>
<body>
  <main class="letterhead">
    <header>
      <div class="brand">
        <span class="brand-dot"></span>
        <div class="brand-name">RIDGEVIEW VETERINARY</div>
        <div class="brand-sub">SURGERY</div>
      </div>
      <ul class="contact">
        <li class="address">
          <svg viewBox="0 0 12 12"><path d="M6 0a4.2 4.2 0 0 0-4.2 4.2C1.8 7.4 6 12 6 12s4.2-4.6 4.2-7.8A4.2 4.2 0 0 0 6 0zm0 5.9a1.7 1.7 0 1 1 0-3.4 1.7 1.7 0 0 1 0 3.4z"/></svg>
          <span>48 Tulloch Road<br>Tallowood Vale, Queensland, 4891</span>
        </li>
        <li>
          <svg viewBox="0 0 12 12"><path d="M2.4 1.2l2 2.2-1 1.4c.7 1.5 2 2.8 3.5 3.5l1.4-1 2.2 2-1.2 1.5C5.4 10.6 1.4 6.6.9 2.4z"/></svg>
          <span>(07 4158 6734)</span>
        </li>
        <li>
          <svg viewBox="0 0 12 12"><path d="M1 3h10v6.5H1zm0 0l5 3.6L11 3" stroke="#fff" stroke-width="0.8"/></svg>
          <span>admin@ridgeviewvets.com.au</span>
        </li>
        <li>
          <svg viewBox="0 0 12 12"><circle cx="6" cy="6" r="5" fill="none" stroke="#0b2d5b" stroke-width="0.9"/><path d="M1 6h10M6 1c-2.4 2.8-2.4 7.2 0 10M6 1c2.4 2.8 2.4 7.2 0 10" fill="none" stroke="#0b2d5b" stroke-width="0.8"/></svg>
          <span>ridgeviewvets.com.au</span>
        </li>
      </ul>
    </header>

    <div class="watermark" aria-hidden="true"></div>

    <article class="letter">
      <p class="salutation">Dear Mr. Smith,</p>
      <p class="body">Lorem ipsum dolor sit amet, consectetur adipiscing elit. Donec orci purus, luctus vitae dignissim eu, iaculis sed purus. Vivamus faucibus, ipsum nec aliquet viverra, leo mauris condimentum ligula, sit amet sagittis enim ligula quis arcu. Nam egestas tortor id nisi porttitor mattis. In tortor ante, ultricies in suscipit a, tempus non massa. Vivamus et auctor mi. Fusce vel massa nulla. Phasellus nec eros mauris, et scelerisque orci.</p>
      <p class="body">Donec malesuada orci vitae nulla accumsan porta a id massa. Quisque accumsan iaculis magna sit amet fringilla. Maecenas consequat, magna eget tincidunt semper, odio nibh rutrum mi, id feugiat ante nisi eu risus. Vestibulum nunc orci, rhoncus a placerat in, ultricies in mi. Cras mattis varius eros, vel fringilla nisi suscipit eget. Quisque scelerisque sagittis nulla at porttitor.</p>
      <p class="body">Sed id augue vitae urna euismod commodo aliquet a quam. Pellentesque arcu velit, cursus et malesuada ut, consequat et diam. Nullam erat sem, rhoncus id ullamcorper vitae, rhoncus et arcu. In ultricies ultricies nulla, ut rutrum nisi iaculis at. Donec eu magna a metus ornare faucibus. Fusce aliquet faucibus ultricies. Morbi semper, est id tincidunt gravida, sem arcu adipiscing lacus, ac bibendum nulla leo eu purus. Quisque nec diam sed risus consectetur a ccumsan quis quis nibh. Vestibulum id purus lorem.</p>
      <p class="closing">Sincerely,</p>
      <span class="signature" role="img" aria-label="Handwritten signature"></span>
    </article>

    <svg class="footer-band" viewBox="0 0 710 131" preserveAspectRatio="none" aria-hidden="true">
      <path d="M0 22 C230 100 500 112 710 11 L710 131 L0 131 Z" fill="#0b2d5b"/>
      <path d="M100 62 C300 108 520 106 710 21" fill="none" stroke="#e6e6ea" stroke-width="1.6"/>
    </svg>
    <footer class="hours"><strong>Monday to Friday</strong> - 8am to 5pm <strong>Saturday</strong> - 8am to 12pm</footer>
  </main>
</body>
</html>
```